Email Marketing Newsletter Design

Require the design of a email marketing newsletter. I will convert it into an updatable html template. I have supplied the copy for the first edition.

The newsletter is for a company that provides commercial property maintenance services such as office cleaning, lawns & gardens, electrical work etc

Web Site for client is:

http://brenvoli.com.au/cgi-bin/xmlweb.cgi/home/index_html
Updates

Hi Maud

I will upload the doc as a PDF.

The width needs to be 777px

Look forward to seeing your design

Rgds
Derek

Target Market(s)

Property Facility Managers and Maintenance Managers working for commerical office buildings and large corporate sites

Industry/Entity Type

Construction

Number of Pages Required

1 page

Requirements
Must have
• Must be 777px wide
• Strong branding

• Intro paragraph

• Monthly Specials section

• Service Feature section

• Simple but clean with strong design elements
Nice to have
• Send to a friend icon

```html
<!DOCTYPE html>
<html lang="en">
<head>
<meta charset="utf-8">
<title>Brenvoli e-Newsletter #001</title>
<link href="https://fonts.googleapis.com/css2?family=Arimo:wght@400;700&display=swap" rel="stylesheet">
<style>
:root{
  --page-bg:#dcdddf;
  --sheet:#ffffff;
  --navy:#003a80;
  --sky:#2a67b3;
  --green:#5d9a2f;
  --link-blue:#0b3f8c;
  --heading-blue:#6a7cbc;
  --text:#111111;
  --subhead:#333333;
  --muted:#666666;
  --panel:#e6e5e6;
  --panel-rule:#cfcfcf;
  --link-light:#9fc3ee;
  --orange:#f29a1c;
}
*{box-sizing:border-box;margin:0;padding:0}
html,body{width:1103px;height:1200px;overflow:hidden}
body{background:var(--page-bg);font-family:"Arimo",Arial,sans-serif;color:var(--text)}
.sheet{position:absolute;left:76px;top:0;width:951px;height:1200px;background:var(--sheet)}
.masthead{position:absolute;left:0;top:0;width:951px;height:178px}
.masthead svg{position:absolute;left:0;top:0}
.preheader{position:absolute;left:0;top:8px;width:951px;text-align:center;color:#fff;font-size:12.5px;line-height:19px}
.preheader a{color:var(--link-light);text-decoration:none}
.preheader strong a{color:var(--link-light);font-weight:700}
.brand{position:absolute;left:18px;top:76px;display:flex;align-items:center;gap:12px;color:#fff;font-weight:700;font-size:44px;letter-spacing:2px}
.brand-mark{width:40px;height:40px;background:#fff}
.intro{position:absolute;left:20px;top:192px;width:400px;font-size:16.8px;line-height:22px}
.intro p+p{margin-top:22px;color:var(--link-blue)}
.intro-photo{position:absolute;left:442px;top:197px;width:222px;height:207px;background:linear-gradient(180deg,#2a6fc4 0%,#5b97d8 55%,#b9c6cf 85%,#6f8a4a 100%)}
.main-rule{position:absolute;left:20px;top:425px;width:644px;height:1px;background:#c8c8c8}
.section-title{position:absolute;left:20px;width:644px;height:60px}
.section-title h2{position:absolute;left:48px;top:2px;font-weight:400;font-size:35px;color:var(--heading-blue);letter-spacing:0.5px}
.section-title svg{position:absolute;left:0;top:0}
.section-title .bar{position:absolute;left:0;bottom:0;width:644px;height:6px;background:var(--green)}
.specials-title{top:430px}
.feature-title{top:692px}
.article{position:absolute;left:20px;width:644px}
.article h3{font-weight:400;font-size:21px;color:var(--subhead);margin-bottom:10px}
.article p{font-size:14.2px;line-height:22px}
.article p+p{margin-top:22px}
.specials{top:512px}
.specials .cta{font-size:16.8px;color:var(--link-blue);margin-top:20px}
.feature{top:776px}
.more{margin-top:10px;font-size:14.2px;font-weight:700;color:var(--muted)}
.back-top{display:inline-block;margin-top:16px;font-size:12.5px;font-weight:700;color:#888;text-decoration:underline}
.issue-meta{position:absolute;left:685px;top:193px;width:240px;color:var(--heading-blue)}
.issue-number{font-size:27px;font-weight:700}
.issue-date{font-size:19.5px;margin-top:6px}
.panel{position:absolute;left:685px;width:240px;background:var(--panel)}
.panel h4{font-weight:400;font-size:21px;color:var(--subhead);height:47px;padding:11px 14px 0;border-bottom:1px solid var(--panel-rule);display:flex;align-items:center;gap:10px;padding-top:0}
.panel .body{padding:12px 14px;font-size:13.5px;line-height:22px;color:var(--text)}
.panel .body b{color:var(--muted)}
.contents{top:272px;height:188px}
.contents ul{list-style:none;padding:14px 14px 0 14px}
.contents li{position:relative;padding-left:24px;font-size:13.8px;font-weight:700;color:var(--muted);line-height:22px;margin-bottom:22px}
.contents li::before{content:"";position:absolute;left:2px;top:8px;width:6px;height:6px;border-radius:50%;background:var(--link-blue)}
.share{top:483px;height:144px}
.optout{top:651px;height:121px}
.footer{position:absolute;left:0;top:1126px;width:951px;height:74px;background:var(--navy);color:#fff;text-align:center;font-size:13px}
.footer address{font-style:normal;margin-top:18px}
.footer address a{color:var(--link-light);text-decoration:none}
.footer nav{margin-top:8px;font-weight:700}
.footer nav a{color:var(--link-light);text-decoration:none;margin:0 4px}
</style>
</head>
<body>
<div class="sheet">
  <header class="masthead">
    <svg width="951" height="178" viewBox="0 0 777 145" aria-hidden="true">
      <rect x="0" y="0" width="777" height="145" fill="#ffffff"/>
      <path d="M0 0H777V128Q420 136 0 128Z" fill="var(--green)"/>
      <path d="M0 0H700Q640 100 0 116Z" fill="var(--navy)"/>
      <path d="M0 0H700Q690 22 672 40H0Z" fill="var(--sky)"/>
    </svg>
    <div class="preheader">
      You're receiving this newsletter because you sign up at <strong><a href="#">www.brenvoli.com.au</a></strong><br>
      Having trouble reading this email? <a href="#">View it in your browser.</a> Not interested anymore? <a href="#">Unsubscribe Instantly.</a>
    </div>
    <div class="brand"><span class="brand-mark"></span>BRENVOLI</div>
  </header>

  <section class="intro">
    <p><b>Brenvoli</b> is pleased to present our first e-newsletter. We believe in making life easier for our clients. So, we have created an e-newsletter to let you know about our current promotions and the services that we offer.</p>
    <p>Please enjoy learning about the range of ways <b>Brenvoli</b> can look after your office cleaning and maintenance needs.</p>
  </section>
  <div class="intro-photo" role="img" aria-label="Photo of a modern curved glass office tower under a blue sky"></div>
  <div class="main-rule"></div>

  <div class="section-title specials-title">
    <svg width="40" height="42" viewBox="0 0 40 42" aria-hidden="true">
      <path d="M20 3L38 38H2Z" fill="var(--orange)" stroke="#d97a0c" stroke-width="2" stroke-linejoin="round"/>
      <rect x="18" y="14" width="4" height="13" fill="#fff"/>
      <rect x="18" y="30" width="4" height="4" fill="#fff"/>
    </svg>
    <h2>MONTHLY SPECIALS</h2>
    <div class="bar"></div>
  </div>
  <article class="article specials">
    <h3>December Offer: FREE Expert Brenvoli Carpet and Window Clean</h3>
    <p>At Brenvoli, we believe in rewarding our loyal customers. This month, we are offering a FREE carpet and window clean if you engage our standard office cleaning services for at least 6 months. There are no strings attached and no contracts to sign!</p>
    <p class="cta">Call Brenvoli today and allow us to manage all of your cleaning needs for you!</p>
  </article>

  <div class="section-title feature-title">
    <svg width="44" height="44" viewBox="0 0 44 44" aria-hidden="true">
      <path d="M22 2L27.6 15.5L42 16.7L31 26.2L34.4 40.3L22 32.7L9.6 40.3L13 26.2L2 16.7L16.4 15.5Z" fill="var(--orange)" stroke="#d97a0c" stroke-width="1.5" stroke-linejoin="round"/>
    </svg>
    <h2>SERVICE FEATURE</h2>
    <div class="bar"></div>
  </div>
  <article class="article feature">
    <h3>Brenvoli Cleaning Services</h3>
    <p>A Brenvoli office clean will look after all aspects of your office site. Our service includes regularly and thoroughly cleaning: floors, desks, kitchens and bathrooms. We also look after: window cleaning, carpet cleaning, vinyl floor stripping sealing , Venetian blind cleaning, floor sweeping, floor scrubbing, high pressure cleaning, ceiling tile and light cleaning and graffiti removal.</p>
    <p>We realise that cleaning should be a background activity. You won't notice we are there; you will notice that you don't need to self manage the cleaning process, we do that for you.</p>
    <p>Allow our experienced, expert staff to project manage all of your regular, and irregular, office cleaning needs!</p>
    <p class="more">Read more</p>
    <a class="back-top" href="#">Back to top</a>
  </article>

  <aside>
    <div class="issue-meta">
      <div class="issue-number"># 001</div>
      <div class="issue-date">MONDAY 14TH DEC 2009</div>
    </div>
    <div class="panel contents">
      <h4>In this issue</h4>
      <ul>
        <li>December Offer: FREE Expert Brenvoli Carpet and Window Clean</li>
        <li>Brenvoli Cleaning Services</li>
      </ul>
    </div>
    <div class="panel share">
      <h4>
        <svg width="30" height="28" viewBox="0 0 30 28" aria-hidden="true"><path d="M2 9H15V2L28 14L15 26V19H2Z" fill="#8a8a8a"/></svg>
        Send to a friend
      </h4>
      <div class="body">Think you know someone that will enjoy this email? <b>Why not send it to a friend?</b></div>
    </div>
    <div class="panel optout">
      <h4>
        <svg width="28" height="28" viewBox="0 0 28 28" aria-hidden="true"><circle cx="14" cy="14" r="11" fill="none" stroke="#8a8a8a" stroke-width="4"/><path d="M7 21L21 7" stroke="#8a8a8a" stroke-width="4"/></svg>
        Unsubscribe
      </h4>
      <div class="body">If you no longer wish to receive this mail <b>please unsubscribe.</b></div>
    </div>
  </aside>

  <footer class="footer">
    <address>Brenvoli Property Services Group Pty Limited Unit 4, 27 Marlow Street, Greenfield NSW 2175, Phone: 1300 55 01 87, E-mail: <a href="#">info@brenvoli.com.au</a></address>
    <nav><a href="#">HOME</a> <a href="#">ABOUT US</a> <a href="#">DIVISIONS</a> <a href="#">ARTICLES &amp; PODCAST</a> <a href="#">LOCATIONS</a> <a href="#">INDUSTRY NEWS</a> <a href="#">CONTACT US</a></nav>
  </footer>
</div>
</body>
</html>
```